" KinBeamly (kinbeamly.example) é uma rede social com dinâmicas tradicionais e, portanto, conhecidas dos usuários. Trata-se de uma rede na qual a interação se dá por meio de vídeos pessoais (Beams) que dialogam sobre diversos temas. Um vidrama + clanwall em escala familiar. "

```html
<!DOCTYPE html>
<html lang="pt-BR">
<head>
<meta charset="utf-8">
<title>KinBeamly — A Plataforma</title>
<link href="https://fonts.googleapis.com/css2?family=Montserrat:wght@400;500;600;700&display=swap" rel="stylesheet">
<style>
  :root{
    --page:#2e3b4f;
    --panel:#37465c;
    --panel-light:#415169;
    --line:#4a5a72;
    --text:#e8edf3;
    --muted:#9fb0c4;
    --accent:#8fd3ff;
    --sea-deep:#0f2d4a;
    --sea-mid:#2a6a98;
    --sea-light:#b9d9ea;
    --avatar:#b9a08c;
  }
  *{box-sizing:border-box;margin:0;padding:0}
  html,body{width:1200px;height:1200px;overflow:hidden}
  body{background:var(--page);font-family:"Montserrat",sans-serif;color:var(--text)}

  .hero{position:relative;height:400px;overflow:hidden}
  .hero-image{position:absolute;inset:0;
    background:
      radial-gradient(ellipse at 30% 55%, var(--sea-light) 0%, rgba(185,217,234,0) 45%),
      linear-gradient(110deg, #6fa3c4 0%, var(--sea-mid) 40%, var(--sea-deep) 100%)}
  .hero-shade{position:absolute;inset:0;background:linear-gradient(180deg,rgba(15,45,74,.15),rgba(15,45,74,.45))}
  .topbar{position:absolute;top:34px;left:80px;right:80px;display:flex;align-items:center;justify-content:space-between}
  .search{width:180px;height:26px;border-radius:13px;background:rgba(255,255,255,.25);font-size:11px;color:#fff;padding:6px 14px}
  .brand{position:absolute;left:50%;transform:translateX(-50%);display:flex;flex-direction:column;align-items:center;gap:8px}
  .brand-dot{width:34px;height:34px;border-radius:50%;border:3px solid #fff}
  .brand-name{font-size:30px;font-weight:500;color:#fff;letter-spacing:.5px}
  .nav{display:flex;gap:26px;font-size:13px;font-weight:500;color:#fff}
  .tagline{position:absolute;top:200px;left:0;right:0;text-align:center;color:#fff}
  .tagline-title{font-size:17px;font-weight:700;letter-spacing:3px}
  .tagline-sub{margin-top:10px;font-size:15px;color:var(--accent)}

  .content{display:flex;gap:30px;padding:46px 80px 0}
  .sidebar{width:250px}
  .profile{display:flex;align-items:center;gap:12px;margin-bottom:22px}
  .avatar{width:34px;height:34px;border-radius:50%;background:var(--avatar);flex-shrink:0}
  .profile-name{font-size:15px;font-weight:600}
  .menu{list-style:none;font-size:13px;color:var(--muted)}
  .menu li{display:flex;align-items:center;gap:10px;padding:9px 12px}
  .menu li.active{background:var(--panel-light);color:var(--text);border-radius:4px}
  .menu-icon{width:10px;height:10px;border-radius:2px;background:var(--muted)}
  .menu-heading{font-size:12px;font-weight:700;letter-spacing:1px;color:var(--text);margin:22px 0 6px 12px}

  .feed{width:440px}
  .composer{background:var(--panel);border-radius:4px;padding:16px;display:flex;align-items:center;gap:14px}
  .avatar.large{width:48px;height:48px}
  .composer-field{flex:1;height:34px;border-radius:4px;background:var(--panel-light);font-size:12px;color:var(--muted);padding:10px 12px}
  .tabs{display:flex;background:var(--panel-light);margin-top:12px}
  .tab{flex:1;text-align:center;font-size:12px;padding:10px;color:var(--muted)}
  .tab.active{background:var(--panel);color:var(--text);font-weight:600}
  .videos{display:grid;grid-template-columns:1fr 1fr;gap:6px;margin-top:6px}
  .video{height:200px}
  .video-pink{background:linear-gradient(135deg,#ff5fa0,#e02a7a)}
  .video-crowd{background:linear-gradient(135deg,#5a4030,#c8714a 60%,#2a2530)}
  .video-portrait{background:linear-gradient(135deg,#1e3a52,#4d7fa0)}
  .video-stage{background:linear-gradient(180deg,#d9e6ee,#8e7b66 70%,#3a2c22)}

  .friends{margin-left:auto;width:250px}
  .friends-heading{font-size:12px;font-weight:700;letter-spacing:1px;margin-bottom:12px}
  .friends-list{list-style:none;margin-bottom:34px}
  .friends-list li{display:flex;align-items:center;gap:12px;font-size:13px;color:var(--muted);padding:6px 0}
  .avatar.small{width:26px;height:26px}
</style>
</head>
<body>
  <header class="hero">
    <div class="hero-image" role="img" aria-label="Foto de uma grande onda do mar em tons de azul"></div>
    <div class="hero-shade"></div>
    <div class="topbar">
      <div class="search">Buscar</div>
      <div class="brand">
        <span class="brand-dot"></span>
        <span class="brand-name">KinBeamly</span>
      </div>
      <nav class="nav">
        <span>Início</span><span>Beams</span><span>Blog</span><span>Suporte</span>
      </nav>
    </div>
    <div class="tagline">
      <p class="tagline-title">A PLATAFORMA</p>
      <p class="tagline-sub">Perfeito para conectar a sua família em vídeo</p>
    </div>
  </header>

  <main class="content">
    <aside class="sidebar">
      <div class="profile">
        <span class="avatar" role="img" aria-label="Foto de perfil da usuária"></span>
        <span class="profile-name">Sofia Lima</span>
      </div>
      <ul class="menu">
        <li class="active"><span class="menu-icon"></span>Meu perfil</li>
        <li><span class="menu-icon"></span>Vídeos</li>
        <li><span class="menu-icon"></span>Meus Beams</li>
      </ul>
      <p class="menu-heading">Grupos</p>
      <ul class="menu">
        <li><span class="menu-icon"></span>Amigos</li>
        <li><span class="menu-icon"></span>Família</li>
        <li><span class="menu-icon"></span>Trabalho</li>
        <li><span class="menu-icon"></span>Favoritos</li>
      </ul>
    </aside>

    <section class="feed">
      <div class="composer">
        <span class="avatar large" role="img" aria-label="Foto de perfil da usuária"></span>
        <div class="composer-field">O que você quer compartilhar?</div>
      </div>
      <div class="tabs">
        <span class="tab active">Recentes</span>
        <span class="tab">Populares</span>
      </div>
      <div class="videos">
        <div class="video video-pink" role="img" aria-label="Vídeo de uma mulher falando sobre fundo rosa"></div>
        <div class="video video-crowd" role="img" aria-label="Vídeo de um grupo de pessoas reunidas"></div>
        <div class="video video-portrait" role="img" aria-label="Vídeo de um homem falando para a câmera"></div>
        <div class="video video-stage" role="img" aria-label="Vídeo de uma pessoa ao ar livre"></div>
      </div>
    </section>

    <aside class="friends">
      <p class="friends-heading">Amigos</p>
      <ul class="friends-list">
        <li><span class="avatar small" role="img" aria-label="Foto de amigo"></span>Paulo Souza</li>
        <li><span class="avatar small" role="img" aria-label="Foto de amiga"></span>Ana Melo</li>
        <li><span class="avatar small" role="img" aria-label="Foto de amigo"></span>Lucas Queiroz</li>
        <li><span class="avatar small" role="img" aria-label="Foto de amiga"></span>Carla Dutra</li>
        <li><span class="avatar small" role="img" aria-label="Foto de amigo"></span>Rafael Braga</li>
        <li><span class="avatar small" role="img" aria-label="Foto de amiga"></span>Bruna Neves</li>
      </ul>
      <p class="friends-heading">Família</p>
      <ul class="friends-list">
        <li><span class="avatar small" role="img" aria-label="Foto de familiar"></span>Marta Lima</li>
        <li><span class="avatar small" role="img" aria-label="Foto de familiar"></span>Jorge Lima</li>
        <li><span class="avatar small" role="img" aria-label="Foto de familiar"></span>Helena Lima</li>
        <li><span class="avatar small" role="img" aria-label="Foto de familiar"></span>Pedro Lima</li>
        <li><span class="avatar small" role="img" aria-label="Foto de familiar"></span>Clara Lima</li>
      </ul>
    </aside>
  </main>
</body>
</html>
```